New email newsletter banner needed

Financial services firm need a new banner for a newsletter banner. The old one attached.... Size is 4cm x 16cm and should read "Looking for Options".

Base colors can be Pantone colors 281,644,425,1805,405 and any gradient of those.

Font should be Arial MT

Please note the firm mentioned in the old banner no longer applies

Industry/Entity Type

Financial

Requirements
Should not have
• images of people, multiple images

```html
<!DOCTYPE html>
<html lang="en">
<head>
<meta charset="utf-8">
<title>Looking for Options – Newsletter Banner</title>
<link rel="stylesheet" href="https://fonts.googleapis.com/css2?family=Arimo:wght@400&display=swap">
<style>
  :root {
    --sky-light: #7faad0;
    --sky-mid: #4f7fb8;
    --navy-deep: #163577;
    --headline-grey: #4a4a4c;
    --headline-glow: rgba(255, 255, 255, 0.95);
    --art-green: #8fc46a;
    --art-skin: #f1c98e;
    --art-edge: #111111;
  }

  html, body {
    margin: 0;
    padding: 0;
    width: 1200px;
    height: 300px;
    overflow: hidden;
    background: #ffffff;
  }

  .banner {
    position: relative;
    width: 1200px;
    height: 300px;
    overflow: hidden;
    background: linear-gradient(90deg,
      var(--sky-light) 0%,
      var(--sky-mid) 45%,
      var(--navy-deep) 100%);
  }

  .banner__headline {
    position: absolute;
    left: 60px;
    top: 92px;
    margin: 0;
    font-family: "Arimo", Arial, sans-serif;
    font-weight: 400;
    font-size: 88px;
    line-height: 1;
    letter-spacing: -0.5px;
    color: var(--headline-grey);
    text-shadow:
      0 0 6px var(--headline-glow),
      0 0 14px rgba(255, 255, 255, 0.7);
    white-space: nowrap;
  }

  .banner__art {
    position: absolute;
    left: 946px;
    top: 19px;
    width: 246px;
    height: 266px;
    border-radius: 10px;
    background: linear-gradient(160deg,
      var(--art-green) 0%,
      var(--art-green) 45%,
      var(--art-skin) 70%,
      #ffffff 100%);
    box-shadow: inset 0 0 0 3px var(--art-edge);
  }
</style>
</head>
<body>
  <header class="banner">
    <h1 class="banner__headline">Looking for Options</h1>
    <div class="banner__art" role="img" aria-label="Illustration of a hand holding a fan of green dollar bills"></div>
  </header>
</body>
</html>
```